Design packaging for our 'Marlowen Drift' personal massager (vibrator)!

Design our product box, please.

We will be selling a vibrator (personal massager on the website:-) ) in 4 different colours - please see attached. The box will be matt black, and we would love classy and understated, definitely not garish or raunchy. Note that the Barcode has to be on a white background, so we suspect we will need to stick that onto the box somewhere - probably the bottom, unless anyone has a better (more aesthetically pleasing) idea! Dimensions of the barcode must be between 1 inch x 2 inches and 2 inches x 3 inches(1 inch x 3 inches, or 2 inches by 2 inches, for eg) - if you can propose a spot, that would be great. The product has a pink satin travel pouch in the box, and product comes in pink, purple, Rose and Black. The box needs to stand out in photography, and the product will be sold online. Could add 'Heated Massager' somewhere, and colour of the product, too. Certifications that would be good to have on the box: CE and ROHS. There is a small insert box for the charger wire - would want 'Charger Wire' in matching script on this box. Script to match product name, please.

We included a potential logo for the box, and also our company logo. We are open to suggestions on the logo for the box, but the product name is Marlowen Drift (spelling intentionally different from Co. name), and it should tie in with our company logo in some way.

We will be super quick in obtaining any additional information required from the supplier, or answering any questions.

Target Market(s)

Audience: Mostly women (of all ages, hopefully)! Realistically, they'll be between the ages of 18 and 40 for the most part. They will be American (that's where our market is, but we anticipate moving to UK, Australia and Europe. Middle to high income earners. We expect they will be looking for subtlety and quality.

Font styles to use
Other font styles liked:
• See Product name logo attachment

Colors

Designer to choose colors to be used in the design.

Requirements
Must have
• Convey quality, understatement and link to our company logo in some way. Should stand out when photographed, and compared to competitors on online forum!
Should not have
• Crass, raunchy feel. No pictures of vibrators.

```html
<!DOCTYPE html>
<html lang="en">
<head>
<meta charset="utf-8">
<title>Marlowen Drift – Box Dielines</title>
<link href="https://fonts.googleapis.com/css2?family=Oswald:wght@400;500&display=swap" rel="stylesheet">
<style>
  :root{
    --paper:#ffffff;
    --box-black:#333333;
    --ink:#111111;
    --brand-violet:#7e4fb4;
    --pink-a:#ff0a78;
    --pink-b:#f200d4;
    --purple-a:#f20ab4;
    --purple-b:#d900ee;
    --pink-accent:#e2208f;
    --purple-accent:#b0128f;
    --band-pink:#ff0a78;
    --band-purple:#f00cb8;
  }
  html,body{margin:0;padding:0;overflow:hidden;}
  body{width:1200px;height:954px;background:var(--paper);position:relative;font-family:'Oswald',sans-serif;}
  .variant-label{position:absolute;top:104px;font-size:19px;letter-spacing:5px;color:#111;font-weight:400;margin:0;}
  .dieline{position:absolute;top:147px;width:403px;height:717px;}
  .dieline svg{position:absolute;left:0;top:0;}
  .front{position:absolute;left:123px;width:157px;text-align:center;}
  .company{top:150px;}
  .company .dot{width:18px;height:18px;border-radius:50%;background:var(--brand-violet);margin:0 auto 8px;}
  .company .name{color:var(--brand-violet);font-size:19px;font-weight:500;letter-spacing:.5px;line-height:1;}
  .product-word{position:absolute;left:133px;font-size:84px;font-weight:500;line-height:1;margin:0;
    background:linear-gradient(100deg,#000 0%,#1a1a1a 45%,#6a6a6a 80%,#1d1d1d 100%);
    -webkit-background-clip:text;background-clip:text;color:transparent;letter-spacing:-1px;}
  .product-sub{position:absolute;left:133px;top:513px;font-size:58px;font-weight:400;line-height:1;margin:0;}
  .band-text{top:577px;font-size:12.5px;letter-spacing:2.6px;line-height:24px;}
  .feature{position:absolute;left:280px;width:123px;text-align:center;}
  .feature svg{position:static;display:block;margin:0 auto;}
  .feature span{display:block;font-size:8.5px;letter-spacing:1.6px;line-height:10px;margin-top:11px;}
  .pink .product-sub{color:var(--pink-accent);}
  .pink .band-text,.pink .feature span{color:#c4006a;}
  .purple .product-sub{color:var(--purple-accent);}
  .purple .band-text,.purple .feature span{color:#a0087e;}
</style>
</head>
<body>

<p class="variant-label" style="left:112px">PINK</p>
<p class="variant-label" style="left:686px">PURPLE</p>

<!-- Pink box -->
<section class="dieline pink" style="left:112px">
  <svg width="403" height="717" viewBox="0 0 403 717">
    <defs>
      <linearGradient id="pinkFill" x1="1" y1="0" x2="0" y2="1">
        <stop offset="0" stop-color="var(--pink-a)"/>
        <stop offset="1" stop-color="var(--pink-b)"/>
      </linearGradient>
    </defs>
    <g fill="url(#pinkFill)">
      <polygon points="18,87 118,87 124,116 18,116"/>
      <polygon points="285,87 386,87 386,116 279,116"/>
      <rect x="0" y="119" width="123" height="479"/>
      <rect x="280" y="119" width="123" height="479"/>
      <polygon points="18,601 123,601 117,630 18,630"/>
      <polygon points="280,601 386,601 386,630 286,630"/>
    </g>
    <g stroke="rgba(255,255,255,.28)" stroke-width="1" fill="none">
      <rect x="45.5" y="117.5" width="78" height="481"/>
      <rect x="280.5" y="117.5" width="78" height="481"/>
    </g>
    <path fill="var(--box-black)" d="M125 0H278V37H278Q280 40 280 46V601V670Q280 681 278 681V717H125V681Q123 681 123 670V46Q123 40 125 37Z"/>
    <rect x="123" y="574" width="157" height="27" fill="var(--band-pink)"/>
  </svg>
  <div class="front company"><div class="dot"></div><div class="name">HALCYON DIRECT LLC</div></div>
  <p class="product-word" style="top:245px">MAR</p>
  <p class="product-word" style="top:339px">LOW</p>
  <p class="product-word" style="top:435px">EN</p>
  <p class="product-sub">DRIFT</p>
  <div class="front band-text">HEATED MASSAGER</div>
  <div class="feature" style="top:200px">
    <svg width="44" height="44" viewBox="0 0 44 44" fill="none" stroke="#c4006a" stroke-opacity=".55" stroke-width="1.6"><circle cx="22" cy="22" r="21"/><path d="M19.5 10a2.5 2.5 0 0 1 5 0v14a5 5 0 1 1-5 0z"/><circle cx="22" cy="28" r="2.2" fill="#c4006a" fill-opacity=".55"/></svg>
    <span>HEATED<br>MASSAGER</span>
  </div>
  <div class="feature" style="top:329px">
    <svg width="44" height="44" viewBox="0 0 44 44" fill="none" stroke="#c4006a" stroke-opacity=".55" stroke-width="1.6"><circle cx="22" cy="22" r="21"/><path d="M17 17l10 10M19 14l-5 5a5 5 0 0 0 7 7l5-5M24 13l3 3M28 17l3 3M14 30l-3 3"/></svg>
    <span>CHARGER<br>WIRE</span>
  </div>
  <div class="feature" style="top:457px">
    <svg width="44" height="44" viewBox="0 0 44 44" fill="none" stroke="#c4006a" stroke-opacity=".55" stroke-width="1.6"><circle cx="22" cy="22" r="21"/><text x="22" y="25" text-anchor="middle" font-family="Oswald,sans-serif" font-size="8" letter-spacing="1.2" fill="#c4006a" fill-opacity=".55" stroke="none">ICON</text></svg>
    <span>TEXT</span>
  </div>
</section>

<!-- Purple box -->
<section class="dieline purple" style="left:686px">
  <svg width="403" height="717" viewBox="0 0 403 717">
    <defs>
      <linearGradient id="purpleFill" x1="1" y1="0" x2="0" y2="1">
        <stop offset="0" stop-color="var(--purple-a)"/>
        <stop offset="1" stop-color="var(--purple-b)"/>
      </linearGradient>
    </defs>
    <g fill="url(#purpleFill)">
      <polygon points="18,87 118,87 124,116 18,116"/>
      <polygon points="285,87 386,87 386,116 279,116"/>
      <rect x="0" y="119" width="123" height="479"/>
      <rect x="280" y="119" width="123" height="479"/>
      <polygon points="18,601 123,601 117,630 18,630"/>
      <polygon points="280,601 386,601 386,630 286,630"/>
    </g>
    <g stroke="rgba(255,255,255,.28)" stroke-width="1" fill="none">
      <rect x="45.5" y="117.5" width="78" height="481"/>
      <rect x="280.5" y="117.5" width="78" height="481"/>
    </g>
    <path fill="var(--box-black)" d="M125 0H278V37H278Q280 40 280 46V601V670Q280 681 278 681V717H125V681Q123 681 123 670V46Q123 40 125 37Z"/>
    <rect x="123" y="574" width="157" height="27" fill="var(--band-purple)"/>
  </svg>
  <div class="front company"><div class="dot"></div><div class="name">HALCYON DIRECT LLC</div></div>
  <p class="product-word" style="top:245px">MAR</p>
  <p class="product-word" style="top:339px">LOW</p>
  <p class="product-word" style="top:435px">EN</p>
  <p class="product-sub">DRIFT</p>
  <div class="front band-text">HEATED MASSAGER</div>
  <div class="feature" style="top:200px">
    <svg width="44" height="44" viewBox="0 0 44 44" fill="none" stroke="#a0087e" stroke-opacity=".6" stroke-width="1.6"><circle cx="22" cy="22" r="21"/><path d="M19.5 10a2.5 2.5 0 0 1 5 0v14a5 5 0 1 1-5 0z"/><circle cx="22" cy="28" r="2.2" fill="#a0087e" fill-opacity=".6"/></svg>
    <span>HEATED<br>MASSAGER</span>
  </div>
  <div class="feature" style="top:329px">
    <svg width="44" height="44" viewBox="0 0 44 44" fill="none" stroke="#a0087e" stroke-opacity=".6" stroke-width="1.6"><circle cx="22" cy="22" r="21"/><path d="M17 17l10 10M19 14l-5 5a5 5 0 0 0 7 7l5-5M24 13l3 3M28 17l3 3M14 30l-3 3"/></svg>
    <span>CHARGER<br>WIRE</span>
  </div>
  <div class="feature" style="top:457px">
    <svg width="44" height="44" viewBox="0 0 44 44" fill="none" stroke="#a0087e" stroke-opacity=".6" stroke-width="1.6"><circle cx="22" cy="22" r="21"/><text x="22" y="25" text-anchor="middle" font-family="Oswald,sans-serif" font-size="8" letter-spacing="1.2" fill="#a0087e" fill-opacity=".6" stroke="none">ICON</text></svg>
    <span>TEXT</span>
  </div>
</section>

</body>
</html>
```